New Advertising Company Business Card

A two sided business card. One side with logo only and the other side with my information and maybe my logo again. Looking for something unique and creative, but not too busy. Info would include my name(Marcus Feldon), President, phone number, address, email address, and website. LOGO IS THE BLUE AND WHITE ONE.

Target Market(s)

CEO/VP Level Audience

Industry/Entity Type

Business

Contact Information for Business Card

In Description.

```html
<!DOCTYPE html>
<html lang="en">
<head>
<meta charset="utf-8">
<title>Northgate Advertising – Business Card</title>
<link href="https://fonts.googleapis.com/css2?family=Lato:wght@400;700&display=swap" rel="stylesheet">
<style>
  :root{
    --backdrop:#2b2b2b;
    --card-dark:#222224;
    --brand-blue:#2a73b5;
    --band-dark:#232323;
    --paper:#f0f0f0;
    --ink:#3a3a3a;
    --white:#ffffff;
  }
  *{box-sizing:border-box;margin:0;padding:0}
  html,body{width:1200px;height:716px;overflow:hidden;background:var(--backdrop)}
  body{font-family:"Lato",sans-serif;position:relative}
  .card{position:absolute;top:203px;width:540px;height:310px;border-radius:18px;overflow:hidden;box-shadow:0 14px 30px rgba(0,0,0,.45)}
  .card-back{left:40px;background:var(--card-dark)}
  .card-front{left:620px;background:var(--paper)}
  .card svg.shapes{position:absolute;inset:0}

  .brand{position:absolute;display:flex;align-items:center;gap:10px;font-weight:700;letter-spacing:.12em;text-transform:uppercase;font-size:21px}
  .brand-mark{width:14px;height:14px;border-radius:50%;background:var(--brand-blue);flex:none}
  .card-back .brand{left:0;right:0;top:118px;justify-content:center;color:var(--white)}
  .card-back .website{position:absolute;left:0;right:0;top:160px;text-align:center;color:var(--brand-blue);font-size:14px}

  .card-front .brand{left:40px;top:78px;color:var(--white);font-size:20px;line-height:26px}
  .card-front .brand-name{display:block}
  .card-front .brand-mark{background:var(--white)}
  .card-front .website{position:absolute;left:34px;top:176px;color:var(--white);font-size:14px}

  .person{position:absolute;right:34px;top:52px;text-align:right}
  .person .name{font-size:24px;color:var(--ink)}
  .person .title{font-size:12px;color:var(--brand-blue);margin-top:2px}

  .contact{position:absolute;right:34px;top:130px;list-style:none;text-align:right;color:var(--ink);font-size:14px;line-height:24px}
  .contact li{display:flex;justify-content:flex-end;align-items:center;gap:8px}
  .contact svg{width:13px;height:13px;fill:var(--brand-blue)}

  .social{position:absolute;right:34px;top:232px;color:var(--white);font-size:14px}
</style>
</head>
<body>

<section class="card card-back" aria-label="Card back">
  <div class="brand"><span class="brand-mark"></span>Northgate Advertising</div>
  <p class="website">www.northgateads.com</p>
</section>

<section class="card card-front" aria-label="Card front">
  <svg class="shapes" viewBox="0 0 540 310" aria-hidden="true">
    <path d="M0 0H325Q225 150 120 310H0Z" fill="var(--brand-blue)"/>
    <path d="M318 45Q232 175 150 310H168Q248 182 318 45Z" fill="var(--brand-blue)"/>
    <path d="M0 168H225L206 198H0Z" fill="var(--band-dark)"/>
    <path d="M196 225H540V255H178Z" fill="var(--band-dark)"/>
  </svg>

  <div class="brand"><span class="brand-mark"></span><span class="brand-name">Northgate<br>Advertising</span></div>
  <p class="website">www.northgateads.com</p>

  <div class="person">
    <p class="name">Marcus Feldon</p>
    <p class="title">President</p>
  </div>

  <ul class="contact">
    <li>555 014 2290
      <svg viewBox="0 0 16 16"><path d="M3 1h3l1.5 4-2 1.2a9 9 0 0 0 4.3 4.3L11 8.5l4 1.5v3a2 2 0 0 1-2 2A12 12 0 0 1 1 3a2 2 0 0 1 2-2z"/></svg></li>
    <li>hello@northgateads.com
      <svg viewBox="0 0 16 16"><path d="M1 3h14v10H1z M1 3l7 6 7-6" stroke="#f0f0f0" stroke-width="1.2"/></svg></li>
    <li>120 Harbor Lane, 0000
      <svg viewBox="0 0 16 16"><path d="M8 0a5.5 5.5 0 0 0-5.5 5.5C2.5 10 8 16 8 16s5.5-6 5.5-10.5A5.5 5.5 0 0 0 8 0zm0 8a2.5 2.5 0 1 1 0-5 2.5 2.5 0 0 1 0 5z"/></svg></li>
  </ul>

  <p class="social">/northgateads</p>
</section>

</body>
</html>
```